The Brightwater Compass Business Card

We need an attractive business card with the logo that we bought from ArtVantly last year.
Our mission is to contribute to change the way today's leaders manage business companies bringing value to the workplace and helping them to build a new model of creating wealth.
Our logo is clear about our values : we seek Positive Change through People and are convinced that the pursuit of individual well-being and the chase of economic results can converge with the right management.
Management Consulting
Corinne Fabrelle
+34 612 98 70 31
corinne.fabrelle@thebrightwatercompass-mail.net
www.thebrightwatercompass-mail.net

```html
<!DOCTYPE html>
<html lang="en">
<head>
<meta charset="utf-8">
<title>The Brightwater Compass – Business Card</title>
<link rel="stylesheet" href="https://fonts.googleapis.com/css2?family=Open+Sans:wght@400;600&display=swap">
<style>
  :root {
    --teal: #0f8a84;
    --teal-deep: #0b6f6b;
    --teal-light: #5fb3ae;
    --paper: #ffffff;
    --ink: #4a4a4a;
    --slate: #6e6f70;
    --slate-text: #dcdcdc;
    --backdrop: #2b2b2d;
  }
  * { box-sizing: border-box; margin: 0; padding: 0; }
  html, body {
    width: 1200px; height: 950px; overflow: hidden;
    background: var(--backdrop);
    font-family: "Open Sans", Arial, sans-serif;
  }
  .canvas {
    width: 1200px; height: 950px;
    display: flex; flex-direction: column; align-items: center; justify-content: center;
    gap: 40px;
  }
  .card {
    position: relative;
    width: 700px; height: 400px;
    overflow: hidden;
    box-shadow: 0 10px 30px rgba(0,0,0,.45);
  }
  /* Front */
  .card--front { background: var(--paper); }
  .front-waves { position: absolute; inset: 0; }
  .holder-name {
    position: absolute; top: 24px; right: 44px;
    color: var(--paper); font-size: 26px; font-weight: 400;
  }
  .brand {
    position: absolute; left: 165px; top: 192px;
    display: flex; align-items: center; gap: 14px;
  }
  .brand-dot {
    width: 30px; height: 30px; border-radius: 50%;
    background: var(--teal);
  }
  .brand-name {
    color: var(--teal); font-size: 24px; font-weight: 400;
    letter-spacing: 2px; text-transform: uppercase;
  }
  .contact-list {
    position: absolute; left: 185px; top: 262px;
    list-style: none; display: flex; flex-direction: column; gap: 9px;
  }
  .contact-item {
    display: flex; align-items: center; gap: 10px;
    color: var(--ink); font-size: 15px;
  }
  .contact-icon { width: 16px; height: 16px; flex: none; }
  /* Back */
  .card--back {
    background: var(--slate);
    display: flex; flex-direction: column; align-items: center; justify-content: center;
    gap: 26px;
  }
  .back-brand { display: flex; align-items: center; gap: 16px; }
  .back-brand .brand-dot { background: var(--paper); width: 34px; height: 34px; }
  .back-brand .brand-name { color: var(--paper); font-size: 30px; }
  .back-rule { width: 360px; height: 1px; background: var(--slate-text); }
  .back-web {
    color: var(--slate-text); font-size: 15px; letter-spacing: 3px;
  }
</style>
</head>
<body>
<main class="canvas">
  <section class="card card--front" aria-label="Card front">
    <svg class="front-waves" viewBox="0 0 700 400" width="700" height="400" aria-hidden="true">
      <path d="M0,0 H700 V98 C490,98 250,110 140,185 C90,222 65,310 58,400 H0 Z" fill="var(--teal-light)" opacity=".55"/>
      <path d="M0,0 H700 V80 C480,80 230,90 120,170 C70,210 45,300 35,400 H0 Z" fill="var(--teal)"/>
      <path d="M0,0 H700 V64 C470,64 210,74 100,155 C52,195 28,290 15,400 H0 Z" fill="var(--teal-deep)" opacity=".35"/>
    </svg>
    <p class="holder-name">Corinne Fabrelle</p>
    <div class="brand">
      <span class="brand-dot"></span>
      <span class="brand-name">The Brightwater Compass</span>
    </div>
    <ul class="contact-list">
      <li class="contact-item">
        <svg class="contact-icon" viewBox="0 0 16 16"><path d="M3 1h3l1.5 4-2 1.3a9 9 0 0 0 4.2 4.2L11 8.5l4 1.5v3a2 2 0 0 1-2 2A12 12 0 0 1 1 3a2 2 0 0 1 2-2z" fill="var(--teal)"/></svg>
        <span>+34 612 98 70 31</span>
      </li>
      <li class="contact-item">
        <svg class="contact-icon" viewBox="0 0 16 16"><rect x="1" y="3" width="14" height="10" rx="1" fill="var(--teal)"/><path d="M1.5 3.5 8 9l6.5-5.5" fill="none" stroke="#fff" stroke-width="1.2"/></svg>
        <span>corinne.fabrelle@thebrightwatercompass-mail.net</span>
      </li>
      <li class="contact-item">
        <svg class="contact-icon" viewBox="0 0 16 16"><circle cx="8" cy="8" r="7" fill="var(--teal)"/><path d="M1 8h14M8 1c-3 3.5-3 10.5 0 14M8 1c3 3.5 3 10.5 0 14" fill="none" stroke="#fff" stroke-width="1"/></svg>
        <span>www.thebrightwatercompass-mail.net</span>
      </li>
    </ul>
  </section>

  <section class="card card--back" aria-label="Card back">
    <div class="back-brand">
      <span class="brand-dot"></span>
      <span class="brand-name">The Brightwater Compass</span>
    </div>
    <div class="back-rule"></div>
    <p class="back-web">thebrightwatercompass-mail.net</p>
  </section>
</main>
</body>
</html>
```